Real Estate Wordpress Landing Page

I'm looking to a landing page dedicated to my real estate brokerage that's catered to promoting that my company provides 1.5% listings to home sellers... I have a couple examples that I'm really looking towards mocking in a version with similar color schemes using my current company colors/website.

http://lorvanta.com/
https://www.bluthorn.com/about/one-percent-listing-fee

My brokerage company website is http://www.calmridge.us/

Target Market(s)

real estate home sellers & buyers

Industry/Entity Type

Real Estate

Coding

Coded - Design and coding required

Number of Pages Required

1 page

Colors
3176b5
0255a3
eaf1f7
cedeed

Requirements
Must have
• Company website colors - http://www.calmridge.us/
• Something around the lines of this website page - http://lorvanta.com/
• Wordpress compatibility

```html
<!DOCTYPE html>
<html lang="en">
<head>
<meta charset="utf-8">
<title>Calmridge Realty – List for 1.5% Commission</title>
<link href="https://fonts.googleapis.com/css2?family=Roboto:wght@400;500;700;900&family=Open+Sans:ital,wght@0,400;0,600;0,700;1,400;1,600&display=swap" rel="stylesheet">
<style>
:root{
  --blue:#3176b5;
  --navy:#0255a3;
  --pale:#eaf1f7;
  --mist:#cedeed;
  --green:#5cb82e;
  --ink:#222;
  --text:#555;
  --grey-bg:#f3f3f3;
  --card-cream:#fdfcf3;
  --footer:#141414;
}
*{box-sizing:border-box;margin:0;padding:0}
html,body{width:1200px;height:3991px;overflow:hidden}
body{font-family:"Open Sans",Arial,sans-serif;color:var(--text);background:#fff;position:relative}
h1,h2,h3{font-family:"Roboto",Arial,sans-serif}
.section{position:absolute;left:0;width:1200px}

/* header */
.site-header{top:0;height:115px;background:#fff;z-index:3}
.brand{position:absolute;left:100px;top:0;width:255px;height:195px;background:#fff;border-radius:0 0 128px 128px;display:flex;align-items:center;justify-content:center;gap:10px;z-index:4}
.brand-dot{width:20px;height:20px;background:var(--navy)}
.brand-name{font-family:"Roboto",Arial,sans-serif;font-weight:700;font-size:26px;color:var(--navy)}
.header-contact{position:absolute;right:410px;top:16px;text-align:right;font-family:"Roboto",Arial,sans-serif;line-height:20px}
.header-contact small{display:block;font-size:13px;color:#333}
.header-contact strong{font-size:19px;color:var(--navy)}
.phone-badge{position:absolute;left:798px;top:20px;width:34px;height:34px;border-radius:50%;background:var(--navy);display:flex;align-items:center;justify-content:center}
.search-box{position:absolute;left:855px;top:22px;width:212px;height:30px;border:1px solid #ccc;border-radius:16px;font-size:12px;color:#999;padding:6px 14px}
.search-box svg{position:absolute;right:10px;top:7px}
.main-nav{position:absolute;left:422px;top:76px;display:flex;font-family:"Roboto",Arial,sans-serif;font-weight:700;font-size:14px;color:#222}
.main-nav a{color:inherit;text-decoration:none;margin-right:34px}

/* hero */
.hero{top:115px;height:612px;background:linear-gradient(180deg,#6f7e86 0%,#8c9390 35%,#5d6b4c 70%,#3f5030 100%)}
.hero-photo{position:absolute;inset:0}
.hero-shade{position:absolute;inset:0;background:rgba(0,0,0,.18)}
.hero-title{position:absolute;top:310px;width:100%;text-align:center;color:#fff;font-size:46px;font-weight:700;letter-spacing:1px}
.hero-sub{position:absolute;top:370px;width:100%;text-align:center;color:#fff;font-size:30px;font-weight:700;font-family:"Roboto",Arial,sans-serif}
.hero-form{position:absolute;left:210px;top:437px;width:782px;display:grid;grid-template-columns:256px 256px 256px;gap:7px}
.field{height:40px;background:#fff;border:1px solid #ddd;font-size:12px;color:#777;padding:12px 10px;position:relative}
.field.select::after{content:"";position:absolute;right:12px;top:17px;border:5px solid transparent;border-top-color:#444}
.btn-start{height:40px;background:var(--green);color:#fff;font-family:"Roboto",Arial,sans-serif;font-weight:700;font-size:14px;display:flex;align-items:center;justify-content:center;gap:6px}
.hero-arrow{position:absolute;top:290px}

/* welcome */
.welcome{top:727px;height:486px;background:#fff}
.welcome h2{position:absolute;top:75px;width:100%;text-align:center;font-size:32px;color:#222;font-weight:700}
.welcome h2 span{color:var(--navy)}
.welcome p{position:absolute;left:160px;top:135px;width:880px;text-align:center;font-size:13px;line-height:26px;color:#666}

/* blue band */
.band{top:1213px;height:637px;background:linear-gradient(180deg,#2f86c8 0%,#2a7fc2 45%,#3f8ec6 100%)}
.band-photo{position:absolute;left:0;top:200px;width:1200px;height:437px;background:linear-gradient(90deg,rgba(40,120,190,.85),rgba(60,140,200,.7)),linear-gradient(180deg,#5a86a8,#3e6e86)}
.service-cards{position:absolute;top:1030px;left:130px;width:940px;display:flex;gap:22px;z-index:2}
.service-card{width:298px;height:292px;background:#fff;border:1px solid #e3e3e3;padding:22px 28px;box-shadow:0 2px 6px rgba(0,0,0,.08)}
.service-card h3{font-size:19px;font-weight:700;color:#222;line-height:23px;margin:10px 0}
.service-card ul{list-style:none}
.service-card li{font-size:11.5px;line-height:24px;color:#333;padding-left:18px;position:relative}
.service-card li svg{position:absolute;left:0;top:8px}
.video{position:absolute;left:133px;top:1437px;width:422px;height:296px;border:3px solid #fff;background:linear-gradient(135deg,#a7b6c4 0%,#7a8e6c 55%,#4e6b3c 100%)}
.play{position:absolute;left:185px;top:118px;width:54px;height:54px;border-radius:50%;background:#fff;display:flex;align-items:center;justify-content:center}
.promo{position:absolute;left:588px;top:1440px;width:480px;height:290px}
.promo .corner{position:absolute;width:28px;height:28px;border-color:#fff;border-style:solid}
.promo h2{position:absolute;left:32px;top:30px;font-size:56px;line-height:62px;color:#fff;font-weight:900}
.promo p{position:absolute;left:36px;top:166px;color:#fff;font-size:17px;font-style:italic;font-weight:600}
.btn-quote{position:absolute;left:36px;top:212px;width:178px;height:34px;border-radius:17px;background:var(--green);color:#fff;font-family:"Roboto",Arial,sans-serif;font-weight:700;font-size:14px;display:flex;align-items:center;justify-content:center}

/* listings */
.listings{top:1850px;height:990px;background:var(--grey-bg)}
.listings h2{position:absolute;top:88px;width:100%;text-align:center;font-size:32px;color:#222;font-weight:700}
.grid{position:absolute;left:130px;top:205px;display:grid;grid-template-columns:repeat(3,298px);gap:48px 22px}
.property{height:305px;background:var(--card-cream);border:1px solid #e2e2d8}
.property .photo{height:165px;position:relative}
.saved{position:absolute;right:0;top:16px;background:var(--blue);color:#fff;font-size:14px;font-weight:600;padding:5px 12px}
.property p{font-size:11.5px;line-height:20px;color:#333;padding:18px 16px 14px;border-bottom:1px solid #e2e2d8;height:98px}
.property .meta{display:flex;justify-content:space-between;padding:12px 16px;font-size:11.5px;color:#333}
.property .meta span{display:flex;align-items:center;gap:5px}

/* testimonials */
.owners{top:2840px;height:660px;background:#fff}
.owners h2{position:absolute;top:98px;width:100%;text-align:center;font-size:32px;color:#222;font-weight:500}
.owners h2 span{color:var(--navy);font-weight:700}
.owners .rule{position:absolute;left:570px;top:150px;width:60px;height:3px;background:var(--blue)}
.avatar{position:absolute;left:268px;top:210px;width:172px;height:172px;border-radius:50%;border:4px solid #ddd;background:radial-gradient(circle at 50% 45%,#c9d7e6,#7fa2c6)}
.quote{position:absolute;left:510px;top:210px;width:450px}
.quote p{font-style:italic;font-size:16px;line-height:26px;color:#777}
.quote .who{margin-top:22px;font-size:15px;color:#333;line-height:26px}
.city-backdrop{position:absolute;left:0;top:405px;width:1200px;height:145px;background:linear-gradient(180deg,rgba(234,241,247,0) 0%,#eef2f6 60%,rgba(238,242,246,.4) 100%)}
.partners{position:absolute;top:580px;left:160px;width:880px;display:flex;justify-content:space-between;align-items:center}
.partner{height:30px;background:#b9b9b9}

/* footer */
.site-footer{top:3500px;height:491px;background:var(--footer);color:#ddd}
.site-footer h3{font-size:22px;font-weight:700;color:#fff;margin-bottom:22px}
.col{position:absolute;top:60px}
.links{list-style:none}
.links li{font-size:12.5px;line-height:24px;color:#ddd;padding-left:14px;position:relative}
.links li::before{content:"›";position:absolute;left:0;color:#aaa}
.contact-item{display:flex;gap:12px;font-size:12.5px;line-height:18px;margin-bottom:22px}
.quote-form p{font-size:13px;margin-bottom:22px}
.quote-grid{display:grid;grid-template-columns:212px 212px;gap:13px 12px}
.quote-grid div{height:38px;border:1px solid #aaa;font-size:12px;color:#fff;padding:11px 10px}
.btn-submit{margin-top:16px;width:212px;height:38px;background:var(--blue);color:#fff;font-family:"Roboto",Arial,sans-serif;font-weight:700;font-size:15px;display:flex;align-items:center;justify-content:center}
.copyright{position:absolute;left:130px;top:440px;font-size:12px;color:#ccc}
.social{position:absolute;left:968px;top:436px;display:flex;gap:6px}
.social span{width:20px;height:20px;border:1px solid #888;border-radius:50%}
</style>
</head>
<body>

<header class="section site-header">
  <div class="brand"><span class="brand-dot"></span><span class="brand-name">Calmridge Realty</span></div>
  <div class="header-contact"><small>Have any Question?</small><strong>555-210-4471</strong></div>
  <div class="phone-badge"><svg width="16" height="16" viewBox="0 0 24 24"><path fill="#fff" d="M6.6 10.8a15 15 0 0 0 6.6 6.6l2.2-2.2c.3-.3.7-.4 1-.2 1.1.4 2.3.6 3.6.6.6 0 1 .4 1 1V20c0 .6-.4 1-1 1A17 17 0 0 1 3 4c0-.6.4-1 1-1h3.5c.6 0 1 .4 1 1 0 1.3.2 2.5.6 3.6.1.3 0 .7-.2 1z"/></svg></div>
  <div class="search-box">Search Here<svg width="14" height="14" viewBox="0 0 24 24"><circle cx="10" cy="10" r="7" fill="none" stroke="#555" stroke-width="2.5"/><path d="M15 15l6 6" stroke="#555" stroke-width="2.5"/></svg></div>
  <nav class="main-nav"><a>HOME</a><a>ABOUT US</a><a>BUY WITH US</a><a>SELL WITH US</a><a>PROPERTIES</a><a>CONTACT US</a></nav>
</header>

<section class="section hero">
  <div class="hero-photo" role="img" aria-label="Two-storey suburban house with a for-sale sign and garden under a cloudy sky"></div>
  <div class="hero-shade"></div>
  <svg class="hero-arrow" style="left:80px" width="24" height="44" viewBox="0 0 24 44"><path d="M20 2L4 22l16 20" fill="none" stroke="#fff" stroke-width="3"/></svg>
  <svg class="hero-arrow" style="right:80px" width="24" height="44" viewBox="0 0 24 44"><path d="M4 2l16 20L4 42" fill="none" stroke="#fff" stroke-width="3"/></svg>
  <h1 class="hero-title">CALMRIDGE REALTY</h1>
  <div class="hero-sub">LIST FOR 1.5% COMMISSION,</div>
  <form class="hero-form">
    <div class="field">First Name</div><div class="field">Last Name</div><div class="field select">Country</div>
    <div class="field">Your Phone</div><div class="field">Email</div>
    <div class="btn-start">GET STARTED <svg width="14" height="14" viewBox="0 0 24 24"><circle cx="12" cy="12" r="10" fill="none" stroke="#fff" stroke-width="2.5"/><path d="M9 7l5 5-5 5" fill="none" stroke="#fff" stroke-width="2.5"/></svg></div>
  </form>
</section>

<section class="section welcome">
  <h2>WELCOME TO <span>CALMRIDGE REALTY</span></h2>
  <p>Sed ut perspiciatis unde omnis iste natus error sit voluptatem accusantium doloremque laudantium, totam rem aperiam, eaque ipsa quae ab illo inventore veritatis et quasi architecto beatae vitae dicta sunt explicabo. Nemo enim ipsam voluptatem quia voluptas sit aspernatur aut odit aut fugit, sed quia consequuntur magni dolores eos qui ratione voluptatem sequi nesciunt. Neque porro quisquam est, qui dolorem ipsum quia dolor sit amet, consectetur, adipisci velit, sed quia non numquam eius modi tempora</p>
</section>

<section class="section band">
  <div class="band-photo" role="img" aria-label="Faded blue-tinted house exterior behind the commission offer"></div>
</section>

<div class="service-cards">
  <article class="service-card">
    <svg width="40" height="36" viewBox="0 0 40 36"><path d="M2 4h16l18 18-12 12L6 16z" fill="var(--navy)"/><circle cx="10" cy="10" r="3" fill="#fff"/></svg>
    <h3>SELL WITH CALMRIDGE<br>&amp; SAVE $$$</h3>
    <ul>
      <li><svg width="10" height="9" viewBox="0 0 10 9"><path d="M1 5l3 3 5-7" fill="none" stroke="var(--navy)" stroke-width="2"/></svg>Professional Real Estate Photography</li>
      <li><svg width="10" height="9" viewBox="0 0 10 9"><path d="M1 5l3 3 5-7" fill="none" stroke="var(--navy)" stroke-width="2"/></svg>Complimentary Comparative Market<br>Analysis (CMA)</li>
      <li><svg width="10" height="9" viewBox="0 0 10 9"><path d="M1 5l3 3 5-7" fill="none" stroke="var(--navy)" stroke-width="2"/></svg>FREE Consultation with Real Estate<br>Professional</li>
    </ul>
  </article>
  <article class="service-card">
    <svg width="40" height="36" viewBox="0 0 40 36"><path d="M4 18L18 4l14 14v16H4z" fill="none" stroke="var(--navy)" stroke-width="3"/><circle cx="18" cy="21" r="6" fill="none" stroke="var(--blue)" stroke-width="3"/><path d="M22 25l6 6" stroke="var(--blue)" stroke-width="3"/></svg>
    <h3>START YOUR HOME<br>SEARCH WITH US</h3>
    <ul>
      <li><svg width="10" height="9" viewBox="0 0 10 9"><path d="M1 5l3 3 5-7" fill="none" stroke="var(--navy)" stroke-width="2"/></svg>1% Buyer Credit at Closing from Calm<br>Ridge Realty</li>
      <li><svg width="10" height="9" viewBox="0 0 10 9"><path d="M1 5l3 3 5-7" fill="none" stroke="var(--navy)" stroke-width="2"/></svg>Quis Molestie Turpis Dapibus At</li>
      <li><svg width="10" height="9" viewBox="0 0 10 9"><path d="M1 5l3 3 5-7" fill="none" stroke="var(--navy)" stroke-width="2"/></svg>Quis Molestie Turpis Dapibus At</li>
    </ul>
  </article>
  <article class="service-card">
    <svg width="40" height="36" viewBox="0 0 40 36"><rect x="4" y="3" width="28" height="30" fill="none" stroke="var(--navy)" stroke-width="3"/><rect x="9" y="9" width="8" height="8" fill="var(--blue)"/><path d="M20 11h8M9 22h19M9 27h19" stroke="var(--navy)" stroke-width="2.5"/></svg>
    <h3>LEASING &amp; PROPERTY<br>MANAGEMENT</h3>
    <ul>
      <li><svg width="10" height="9" viewBox="0 0 10 9"><path d="M1 5l3 3 5-7" fill="none" stroke="var(--navy)" stroke-width="2"/></svg>We can manage your rental port-<br>folio for you!</li>
      <li><svg width="10" height="9" viewBox="0 0 10 9"><path d="M1 5l3 3 5-7" fill="none" stroke="var(--navy)" stroke-width="2"/></svg>Professional &amp; Experienced Proper-<br>ty Managers</li>
      <li><svg width="10" height="9" viewBox="0 0 10 9"><path d="M1 5l3 3 5-7" fill="none" stroke="var(--navy)" stroke-width="2"/></svg>Receive Top Dollar for your Rental<br>Properties</li>
    </ul>
  </article>
</div>

<div class="video" role="img" aria-label="Video still of a couple meeting an agent in front of a house">
  <div class="play"><svg width="20" height="22" viewBox="0 0 20 22"><path d="M3 2l15 9-15 9z" fill="#222"/></svg></div>
</div>
<div class="promo">
  <span class="corner" style="left:0;top:0;border-width:3px 0 0 3px"></span>
  <span class="corner" style="right:0;top:0;border-width:3px 3px 0 0"></span>
  <span class="corner" style="left:0;bottom:0;border-width:0 0 3px 3px"></span>
  <span class="corner" style="right:0;bottom:0;border-width:0 3px 3px 0"></span>
  <h2>LIST FOR 1.5%<br>COMMISSION,</h2>
  <p>And Receive Top Marketing from Real Estate Pro!</p>
  <div class="btn-quote">REQUEST A QUOTE</div>
</div>

<section class="section listings">
  <h2>PROPERTIES LISTINGS</h2>
  <div class="grid">
    <article class="property"><div class="photo" role="img" aria-label="Two-storey house with lawn" style="background:linear-gradient(180deg,#9fb7cc,#7e8f6c 60%,#4f6e34)"><span class="saved">saved $4,650</span></div><p>Nemo enim ipsam voluptatem quia voluptas sit aspernatur aut odit aut fugit, sed quia consequatur magni dolores eos qui ratione voluptatem</p><div class="meta"><span><svg width="9" height="12" viewBox="0 0 9 12"><path d="M4.5 0A4.5 4.5 0 0 0 0 4.5C0 8 4.5 12 4.5 12S9 8 9 4.5A4.5 4.5 0 0 0 4.5 0z" fill="#555"/><circle cx="4.5" cy="4.5" r="1.6" fill="#fff"/></svg>Los Angeles, California</span><span>$370,000</span></div></article>
    <article class="property"><div class="photo" role="img" aria-label="Suburban home with front lawn" style="background:linear-gradient(180deg,#b8cfe2,#8c8a7c 55%,#5c8a3a)"><span class="saved">saved $4,650</span></div><p>Nemo enim ipsam voluptatem quia voluptas sit aspernatur aut odit aut fugit, sed quia consequatur magni dolores eos qui ratione voluptatem</p><div class="meta"><span><svg width="9" height="12" viewBox="0 0 9 12"><path d="M4.5 0A4.5 4.5 0 0 0 0 4.5C0 8 4.5 12 4.5 12S9 8 9 4.5A4.5 4.5 0 0 0 4.5 0z" fill="#555"/><circle cx="4.5" cy="4.5" r="1.6" fill="#fff"/></svg>Los Angeles, California</span><span>$370,000</span></div></article>
    <article class="property"><div class="photo" role="img" aria-label="Brick family house with garden" style="background:linear-gradient(180deg,#a8bccc,#8a7a66 55%,#567a36)"><span class="saved">saved $4,650</span></div><p>Nemo enim ipsam voluptatem quia voluptas sit aspernatur aut odit aut fugit, sed quia consequatur magni dolores eos qui ratione voluptatem</p><div class="meta"><span><svg width="9" height="12" viewBox="0 0 9 12"><path d="M4.5 0A4.5 4.5 0 0 0 0 4.5C0 8 4.5 12 4.5 12S9 8 9 4.5A4.5 4.5 0 0 0 4.5 0z" fill="#555"/><circle cx="4.5" cy="4.5" r="1.6" fill="#fff"/></svg>Los Angeles, California</span><span>$370,000</span></div></article>
    <article class="property"><div class="photo" role="img" aria-label="Large white house with lawn" style="background:linear-gradient(180deg,#c4d4e2,#a3a69a 55%,#5d8a3c)"><span class="saved">saved $4,650</span></div><p>Nemo enim ipsam voluptatem quia voluptas sit aspernatur aut odit aut fugit, sed quia consequatur magni dolores eos qui ratione voluptatem</p><div class="meta"><span><svg width="9" height="12" viewBox="0 0 9 12"><path d="M4.5 0A4.5 4.5 0 0 0 0 4.5C0 8 4.5 12 4.5 12S9 8 9 4.5A4.5 4.5 0 0 0 4.5 0z" fill="#555"/><circle cx="4.5" cy="4.5" r="1.6" fill="#fff"/></svg>Los Angeles, California</span><span>$370,000</span></div></article>
    <article class="property"><div class="photo" role="img" aria-label="Modern house with pool at dusk" style="background:linear-gradient(180deg,#2d3a52,#8a6a44 55%,#3a8aa8)"><span class="saved">saved $4,650</span></div><p>Nemo enim ipsam voluptatem quia voluptas sit aspernatur aut odit aut fugit, sed quia consequatur magni dolores eos qui ratione voluptatem</p><div class="meta"><span><svg width="9" height="12" viewBox="0 0 9 12"><path d="M4.5 0A4.5 4.5 0 0 0 0 4.5C0 8 4.5 12 4.5 12S9 8 9 4.5A4.5 4.5 0 0 0 4.5 0z" fill="#555"/><circle cx="4.5" cy="4.5" r="1.6" fill="#fff"/></svg>Los Angeles, California</span><span>$370,000</span></div></article>
    <article class="property"><div class="photo" role="img" aria-label="Craftsman house under blue sky" style="background:linear-gradient(180deg,#5f93c8,#9a8e78 55%,#5c8a34)"><span class="saved">saved $4,650</span></div><p>Nemo enim ipsam voluptatem quia voluptas sit aspernatur aut odit aut fugit, sed quia consequatur magni dolores eos qui ratione voluptatem</p><div class="meta"><span><svg width="9" height="12" viewBox="0 0 9 12"><path d="M4.5 0A4.5 4.5 0 0 0 0 4.5C0 8 4.5 12 4.5 12S9 8 9 4.5A4.5 4.5 0 0 0 4.5 0z" fill="#555"/><circle cx="4.5" cy="4.5" r="1.6" fill="#fff"/></svg>Los Angeles, California</span><span>$370,000</span></div></article>
  </div>
</section>

<section class="section owners">
  <div class="city-backdrop" role="img" aria-label="Faint pale city backdrop behind the testimonial"></div>
  <h2>HAPPY <span>HOME OWNERS</span></h2>
  <div class="rule"></div>
  <svg style="position:absolute;left:155px;top:280px" width="18" height="32" viewBox="0 0 18 32"><path d="M15 2L3 16l12 14" fill="none" stroke="#888" stroke-width="3"/></svg>
  <svg style="position:absolute;left:1027px;top:280px" width="18" height="32" viewBox="0 0 18 32"><path d="M3 2l12 14L3 30" fill="none" stroke="#888" stroke-width="3"/></svg>
  <div class="avatar" role="img" aria-label="Portrait of a satisfied client"></div>
  <div class="quote">
    <svg style="position:absolute;left:-60px;top:0" width="46" height="38" viewBox="0 0 46 38"><path d="M2 38V22C2 10 8 3 20 0v6c-6 2-9 6-9 12h9v20zM26 38V22C26 10 32 3 44 0v6c-6 2-9 6-9 12h9v20z" fill="#ddd"/></svg>
    <p>Aociosqu ad litora torquent per conubia nostra per inceptos hymenaeos Proin nulla arcu nonummy luctus dictum eget fermentum et lorem Nunc porta convallis pede</p>
    <svg style="position:absolute;left:400px;top:104px" width="46" height="38" viewBox="0 0 46 38"><path d="M44 0v16c0 12-6 19-18 22v-6c6-2 9-6 9-12h-9V0zM20 0v16C20 28 14 35 2 38v-6c6-2 9-6 9-12H2V0z" fill="#ddd"/></svg>
    <div class="who">Daniel Corvel<br>Calmridge Realty</div>
  </div>
  <div class="partners">
    <span class="partner" style="width:64px"></span>
    <span class="partner" style="width:102px"></span>
    <span class="partner" style="width:100px"></span>
    <span class="partner" style="width:100px"></span>
    <span class="partner" style="width:76px"></span>
    <span class="partner" style="width:106px"></span>
  </div>
</section>

<footer class="section site-footer">
  <div class="col" style="left:130px">
    <h3>QUICK LINKS</h3>
    <ul class="links"><li>Home</li><li>About Us</li><li>Buy With Us</li><li>Sell With Us</li><li>Properties</li><li>Contact Us</li></ul>
  </div>
  <div class="col" style="left:362px">
    <h3>CONTACT US</h3>
    <div class="contact-item"><svg width="11" height="14" viewBox="0 0 9 12"><path d="M4.5 0A4.5 4.5 0 0 0 0 4.5C0 8 4.5 12 4.5 12S9 8 9 4.5A4.5 4.5 0 0 0 4.5 0z" fill="#ddd"/></svg><span>Calmridge Realty<br>742 Harbor Way, Suite 310<br>Westbrook, FL 33999</span></div>
    <div class="contact-item"><svg width="13" height="13" viewBox="0 0 24 24"><path fill="#ddd" d="M6.6 10.8a15 15 0 0 0 6.6 6.6l2.2-2.2c.3-.3.7-.4 1-.2 1.1.4 2.3.6 3.6.6.6 0 1 .4 1 1V20c0 .6-.4 1-1 1A17 17 0 0 1 3 4c0-.6.4-1 1-1h3.5c.6 0 1 .4 1 1 0 1.3.2 2.5.6 3.6.1.3 0 .7-.2 1z"/></svg><span>Phone: 555-210-4471<br>Fax: (555) 580-1190</span></div>
    <div class="contact-item"><svg width="13" height="11" viewBox="0 0 13 11"><rect x="0.5" y="0.5" width="12" height="10" fill="#ddd"/><path d="M1 1l5.5 5L12 1" fill="none" stroke="#141414"/></svg><span>Email: info@calmridge.us</span></div>
  </div>
  <div class="col quote-form" style="left:630px">
    <h3>REQUEST FREE QUOTE</h3>
    <p>Alternatively You Can Fill In The Following Contact Form:</p>
    <div class="quote-grid"><div>Name</div><div>E - Mail</div><div>Phone Number</div><div>Tell Us More</div></div>
    <div class="btn-submit">SUBMIT</div>
  </div>
  <div class="copyright">© 2018 Calmridge Realty . All Rights Reserved.</div>
  <div class="social"><span></span><span></span><span></span><span></span></div>
</footer>

</body>
</html>
```